Podcast Cover Art for rebranded podcast - I have inspiration for the designs

I've had a podcast ("Pocket Full Of Rain") since 2018, but I'm in the process of rebranding it. I've attached the old cover art below, which I loved, but I don't need it to look like that at all. The rebranded podcast is called 'Open Roads with Marta Voss.' I've included the show description at the bottom. I've been working on various design options in Canva, but not obsessed with anything yet, but I'm attaching the ones I do like that I think just need some refining. My very favorite is the one labeled 'favorite_Quiet Hours' so I wouldn't mind keeping that general idea but perfected by a designer. Ultimately, I want something cool, fairly clean, modern, eye catching. I'm into neutrals with maybe a pop of color, so think black, white, grey..maybe silver, and I love a pop of red..and I'm not opposed to other options for the pop color. The show is going to be inspiring, entertaining, and funny. Oh and one other idea I had but I'm not sure if it makes sense with the title and/or what the show is about..but a vinyl record with Quiet Hours with Marta Voss on it somehow, on a record player..not sure.

Ever wonder what it means to truly live authentically? Curious about how to embrace the unpredictability of life? Ready for some heartfelt and lighthearted conversations that inspire and entertain?
Join Marta Voss as she dives into the raw, real, and unscripted moments of life. In each episode, Marta brings candid conversations and genuine insights into the ups and downs we all experience. From personal growth and self-discovery to inspiring stories and valuable life lessons, "Quiet Hours" is a space where authenticity reigns and spontaneity is celebrated.
Whether she's sharing her own journey or chatting with inspiring guests, Marta invites you to explore the beauty of living life without a script. Expect honest reflections, thought-provoking discussions, and a refreshing perspective on navigating life's unpredictable path—all with a dash of fun and humor to keep things lively and entertaining. Step into the unscripted moments of life and tune in for a blend of depth and lightheartedness that will leave you inspired, smiling, and most importantly laughing.

Target Market(s)

25-50 year old women and men (primarily women)

Font styles to use
Sans Serif

Requirements
Should not have
• nothing too feminine or girly, nothing cheesy :)

```html
<!DOCTYPE html>
<html lang="en">
<head>
<meta charset="utf-8">
<title>Open Roads with Marta Voss — Podcast Cover</title>
<link rel="stylesheet" href="https://fonts.googleapis.com/css2?family=Bebas+Neue&family=Kaushan+Script&family=Great+Vibes&family=Poppins:wght@400;800&display=swap">
<style>
  :root {
    --red: #e00a2c;
    --ink: #111111;
    --paper: #f4f2f1;
    --haze: #e9e6e2;
    --leaf: #c9cfae;
    --cream: #e2dccb;
    --shirt: #c81826;
    --shadow: #1c1a19;
    --white: #ffffff;
  }
  html, body {
    margin: 0;
    padding: 0;
    width: 1200px;
    height: 1200px;
    overflow: hidden;
    background: var(--paper);
  }
  .cover {
    position: relative;
    width: 1200px;
    height: 1200px;
    overflow: hidden;
    background: linear-gradient(90deg, var(--paper) 0%, var(--haze) 45%, #e4e0d8 60%);
  }
  .cover-photo {
    position: absolute;
    top: 0;
    left: 520px;
    width: 680px;
    height: 1200px;
    background: linear-gradient(180deg,
      var(--leaf) 0%,
      var(--cream) 22%,
      #d9a49c 34%,
      var(--shirt) 46%,
      #b3131f 62%,
      #3a2f2c 74%,
      var(--shadow) 100%);
    -webkit-mask-image: linear-gradient(90deg, transparent 0%, #000 30%);
    mask-image: linear-gradient(90deg, transparent 0%, #000 30%);
  }
  .title-main {
    position: absolute;
    left: 66px;
    top: 118px;
    margin: 0;
    font-family: "Bebas Neue", "Oswald", sans-serif;
    font-weight: 400;
    font-size: 350px;
    line-height: 1;
    color: var(--red);
    letter-spacing: 2px;
  }
  .title-script {
    position: absolute;
    left: 72px;
    top: 410px;
    margin: 0;
    font-family: "Kaushan Script", cursive;
    font-size: 180px;
    line-height: 1;
    color: var(--ink);
    transform: rotate(-6deg);
    transform-origin: left center;
    -webkit-text-stroke: 14px var(--white);
    paint-order: stroke fill;
  }
  .host-with {
    position: absolute;
    left: 70px;
    top: 668px;
    font-family: "Great Vibes", cursive;
    font-size: 92px;
    line-height: 1;
    color: var(--red);
  }
  .host-first {
    position: absolute;
    left: 70px;
    top: 750px;
    font-family: "Poppins", sans-serif;
    font-weight: 800;
    font-size: 76px;
    line-height: 1;
    color: var(--ink);
  }
  .host-last {
    position: absolute;
    left: 70px;
    top: 824px;
    font-family: "Poppins", sans-serif;
    font-weight: 400;
    font-size: 76px;
    line-height: 1;
    color: var(--ink);
  }
  .show-type {
    position: absolute;
    left: 76px;
    top: 1060px;
    font-family: "Poppins", sans-serif;
    font-weight: 400;
    font-size: 30px;
    letter-spacing: 0.22em;
    color: var(--ink);
  }
</style>
</head>
<body>
  <main class="cover">
    <div class="cover-photo" role="img" aria-label="Photo of the host in a red top and black trousers, leaning laughing against a door frame beside a mirror reflection, in a bright room with palms"></div>
    <h1 class="title-main">OPEN</h1>
    <p class="title-script">Roads</p>
    <span class="host-with">with</span>
    <span class="host-first">MARTA</span>
    <span class="host-last">VOSS</span>
    <span class="show-type">PODCAST</span>
  </main>
</body>
</html>
```